Land Buying Company Needs Letterhead for Direct Mail Marketing to Land Owners

We are looking for a professional letterhead that we will be including in our direct mail marketing. We will be sending this to land owners who may be interested in selling or purchasing land.

The letterhead needs to be editable. Headers and footers would look nice, but we are open. We would want it to include our address, website, phone, and email info. For right now the address to use for design purposes would the following:

Address: 415 Bramwell Avenue #600
Dallas, TX 75219
Website - www.quillridgeacres.example
Email - info@quillridgeacres.example
Phone - 866-402-ACRE

I have attached our logo zip file that we just had done on Pixel Guild. Let me know what questions you have, and thank you.

```html
<!DOCTYPE html>
<html lang="en">
<head>
<meta charset="utf-8">
<title>Quillridge Acres Letterhead</title>
<link href="https://fonts.googleapis.com/css2?family=Montserrat:wght@600&family=Josefin+Sans:wght@700&display=swap" rel="stylesheet">
<style>
  :root {
    --backdrop: #b2b3b2;
    --paper: #ffffff;
    --leaf: #a2c52a;
    --forest: #4f6530;
    --ink: #2b2b2b;
  }
  html, body {
    margin: 0;
    width: 1200px;
    height: 1200px;
    overflow: hidden;
    background: var(--backdrop);
  }
  .letterhead {
    position: absolute;
    left: 294px;
    top: 204px;
    width: 612px;
    height: 793px;
    background: var(--paper);
    box-shadow: 0 0 0 1px #c9cac9;
  }
  .letterhead svg { display: block; width: 100%; height: 100%; }
  .band { fill: var(--leaf); }
  .band-edge { fill: var(--forest); }
  .brand-mark { fill: var(--forest); }
  .brand-name {
    font-family: "Montserrat", sans-serif;
    font-weight: 600;
    fill: var(--forest);
  }
  .contact-box.leaf { fill: var(--leaf); }
  .contact-box.forest { fill: var(--forest); }
  .contact-icon { fill: none; stroke: #fff; stroke-width: 2; stroke-linecap: round; stroke-linejoin: round; }
  .contact-icon.solid { fill: #fff; stroke: none; }
  .contact-text {
    font-family: "Josefin Sans", sans-serif;
    font-weight: 700;
    font-size: 15px;
    fill: var(--ink);
  }
</style>
</head>
<body>
  <div class="letterhead">
    <svg viewBox="473 328 986 1276" preserveAspectRatio="none" aria-label="Quillridge Acres letterhead">
      <g class="header">
        <polygon class="band-edge" points="473,424 559,424 557,428 473,428"/>
        <polygon class="band" points="473,370 584,370 558,425 473,425"/>
        <polygon class="band-edge" points="952,428 1459,428 1459,432 951,432"/>
        <polygon class="band" points="978,374 1459,374 1459,429 951,429"/>

        <circle class="brand-mark" cx="626" cy="408" r="35"/>
        <text class="brand-name" x="680" y="411" font-size="36" textLength="248" lengthAdjust="spacingAndGlyphs">QUILLRIDGE</text>
        <text class="brand-name" x="680" y="434" font-size="17" textLength="246" lengthAdjust="spacing">ACRES</text>
      </g>

      <g class="footer">
        <polygon class="band-edge" points="473,1562 697,1562 698,1566 473,1566"/>
        <polygon class="band" points="473,1508 671,1508 697,1563 473,1563"/>

        <g class="contact phone">
          <rect class="contact-box leaf" x="721" y="1516" width="38" height="37"/>
          <path class="contact-icon" d="M729,1531 q11,-8 22,0 M733,1533 h14 l2,10 h-18 z"/>
          <text class="contact-text" x="777" y="1539" textLength="95" lengthAdjust="spacingAndGlyphs">866-402-ACRE</text>
        </g>

        <g class="contact web">
          <rect class="contact-box forest" x="901" y="1517" width="38" height="37"/>
          <circle class="contact-icon" cx="920" cy="1535" r="9"/>
          <path class="contact-icon" d="M911,1535 h18 M920,1526 q-6,9 0,18 M920,1526 q6,9 0,18"/>
          <text class="contact-text" x="948" y="1531" textLength="235" lengthAdjust="spacingAndGlyphs">WWW.QUILLRIDGEACRES.EXAMPLE</text>
          <text class="contact-text" x="948" y="1549" textLength="240" lengthAdjust="spacingAndGlyphs">INFO@QUILLRIDGEACRES.EXAMPLE</text>
        </g>

        <g class="contact address">
          <rect class="contact-box leaf" x="1212" y="1518" width="38" height="37"/>
          <path class="contact-icon solid" d="M1231,1526 a7,7 0 0 1 7,7 q0,5 -7,14 q-7,-9 -7,-14 a7,7 0 0 1 7,-7 z"/>
          <circle cx="1231" cy="1533" r="2.6" fill="var(--leaf)"/>
          <text class="contact-text" x="1258" y="1531" textLength="182" lengthAdjust="spacingAndGlyphs">415 BRAMWELL AVENUE #600</text>
          <text class="contact-text" x="1258" y="1549" textLength="118" lengthAdjust="spacingAndGlyphs">DALLAS, TX 75219</text>
        </g>
      </g>
    </svg>
  </div>
</body>
</html>
```